Rex Talloway (Flip The Stack) CD Cover Design

Professional Cd cover design needed. No photo of the artist necessary for this cover. You can search Rex Talloway on YouTube for a feel of the artist, inspiration, etc. Song (Flip The Stack)!

Target Market(s)

Big money makers , Hustlers, those who don't mind spending cash.

Colors

Designer to choose colors to be used in the design.

Requirements
Nice to have
• Any symbols related to money.

```html
<!DOCTYPE html>
<html lang="en">
<head>
<meta charset="utf-8">
<title>Flip The Stack – Rex Talloway</title>
<link rel="stylesheet" href="https://fonts.googleapis.com/css2?family=UnifrakturCook:wght@700&family=Alegreya+Sans+SC:wght@400;500&family=Montserrat:wght@800&display=swap">
<style>
  :root {
    --bg-center: #2b2b2b;
    --bg-edge: #0c0c0c;
    --title: #8a8a80;
    --label: #77776d;
    --value: #cfcfcf;
    --artist: #dedede;
    --sparkle: #ffffff;
    --label-mark: #7a2a1a;
  }
  * { margin: 0; padding: 0; box-sizing: border-box; }
  html, body { width: 1200px; height: 1200px; overflow: hidden; background: var(--bg-edge); }
  .cover {
    position: relative;
    width: 1200px;
    height: 1200px;
    overflow: hidden;
  }
  .cover-texture {
    position: absolute;
    inset: 0;
    background: radial-gradient(ellipse at 50% 45%, var(--bg-center) 0%, #1a1a1a 55%, var(--bg-edge) 100%);
  }
  .title-row {
    position: absolute;
    top: 296px;
    left: 0;
    width: 100%;
    display: flex;
    justify-content: center;
    align-items: center;
    gap: 34px;
  }
  .song-title {
    font-family: "UnifrakturCook", "UnifrakturMaguntia", serif;
    font-weight: 700;
    font-size: 86px;
    color: var(--title);
    letter-spacing: 2px;
    line-height: 1;
  }
  .sparkle {
    width: 14px;
    height: 14px;
    border-radius: 50%;
    background: radial-gradient(circle, var(--sparkle) 0%, #bcbcbc 55%, rgba(255,255,255,0) 100%);
    box-shadow: 0 0 8px rgba(255,255,255,0.8);
  }
  .credits {
    position: absolute;
    left: 0;
    width: 100%;
    text-align: center;
    font-family: "Alegreya Sans SC", sans-serif;
    font-weight: 400;
    font-size: 34px;
    color: var(--label);
    line-height: 1;
    white-space: nowrap;
  }
  .credits .value { color: var(--value); }
  .credit-writer { top: 444px; }
  .artist-name {
    font-family: "Montserrat", sans-serif;
    font-weight: 800;
    font-size: 29px;
    color: var(--artist);
    text-transform: uppercase;
    letter-spacing: 1px;
    margin-left: 8px;
  }
  .credit-producer { top: 540px; }
  .credit-artwork { top: 632px; }
  .credit-copyright { top: 724px; }
  .credit-copyright sup { font-size: 22px; vertical-align: 12px; }
  .credit-legal { top: 774px; }
  .credit-executive { top: 866px; }
  .label-mark {
    position: absolute;
    left: 40px;
    top: 1110px;
    display: flex;
    align-items: center;
    gap: 10px;
    font-family: "Alegreya Sans SC", sans-serif;
    font-weight: 500;
    font-size: 30px;
    color: var(--label-mark);
    line-height: 1;
  }
  .label-mark .mark-square {
    width: 18px;
    height: 18px;
    background: var(--label-mark);
  }
</style>
</head>
<body>
  <main class="cover">
    <div class="cover-texture" role="img" aria-label="Dark quilted diamond leather texture"></div>

    <div class="title-row">
      <span class="sparkle"></span>
      <h1 class="song-title">Flip The Stack</h1>
      <span class="sparkle"></span>
    </div>

    <p class="credits credit-writer">Written by: <span class="artist-name">Rex Talloway</span></p>
    <p class="credits credit-producer">Produced by: <span class="value">BeatSmith K for Ember Vault Entertainment, Inc.</span></p>
    <p class="credits credit-artwork">Artwork Provided by: <span class="value">Fjord Studio</span></p>
    <p class="credits credit-copyright"><sup>©</sup> 2018 ALL RIGHTS RESERVED</p>
    <p class="credits credit-legal">Unauthorized Duplication Is A Violation Of Applicable Laws</p>
    <p class="credits credit-executive">Executive Producer: <span class="value">Ember Vault</span></p>

    <div class="label-mark">
      <span class="mark-square"></span>
      <span class="label-name">Ember Vault</span>
    </div>
  </main>
</body>
</html>
```